KirvaLume a new start up looking for packaging design for it's organic Cold pressed Peanut oil.

We require a labelling design for a new company based in the UK called ''KirvaLume''. We will be launching Organic cold pressed peanut oil. We would like a design that is simple yet very catchy and not boring.

Target Market(s)
General consumers and healthy eaters, Vegan friendly

Colors
Designer to choose colors to be used in the design.

Must have
• Refer to Packaging document information for labelling.
• Type of bottle 250 ML Tasbel bottle (refer to Bottle Picture doc.)
• Must have the "KirvaLume" logo stamped somewhere on the front of the package (refer to the Logo document)
• Sleek and appetising design
• Neutral colors possible accents with logo colors
• Claims: Organic, Vegan, High in Monounsaturated fat, High in Poly-unsaturated fat(all this in front of the package)
• Made in the uk logo, and EU organic logo
• Social Media Icons (Instagram,Facebook) as well as website (Kirvalume.co.uk)
• Space reserved at the back of the package for barcode and best before date to be printed on.
Be nice to have: picture of the product on the background if possible

Need extra days to review

Target Market(s)

Font styles to use
Serif
Sans Serif
Decorative
Script

Requirements
Must have

• • Refer to Packaging document information for labelling.

```html
<!DOCTYPE html>
<html lang="en">
<head>
<meta charset="utf-8">
<title>KirvaLume Cold Pressed Peanut Oil – Label</title>
<link rel="stylesheet" href="https://fonts.googleapis.com/css2?family=Lilita+One&family=Josefin+Sans:wght@600&family=Hind:wght@400;500;600&display=swap">
<style>
  :root {
    --paper: #ffffff;
    --kraft: #c49a66;
    --cocoa: #4a1a0c;
    --bark: #6e4524;
    --band: #7b3f1f;
    --leaf: #8cc63f;
    --shell: #b8925c;
    --kernel: #8f2f3a;
  }
  * { margin: 0; padding: 0; box-sizing: border-box; }
  html, body { width: 1200px; height: 1200px; overflow: hidden; background: var(--paper); }
  .label {
    position: relative; width: 1200px; height: 1200px;
    background: var(--paper);
    font-family: "Hind", sans-serif; color: var(--bark);
  }
  .label__body { position: absolute; left: 0; top: 260px; width: 1200px; height: 940px; background: var(--kraft); }
  .label__arch {
    position: absolute; left: 363px; top: 32px; width: 475px; height: 320px;
    background: var(--kraft); border-radius: 237px 237px 0 0;
  }
  .brand-name {
    position: absolute; left: 363px; top: 82px; width: 475px; text-align: center;
    font-family: "Lilita One", sans-serif; font-size: 66px; line-height: 1; color: var(--cocoa);
  }
  .mascot {
    position: absolute; left: 508px; top: 175px; width: 161px; height: 252px;
    border-radius: 80px 80px 50px 50px;
    background: linear-gradient(180deg, #6a2c14 0%, #4f1d0d 60%, #e8b98c 100%);
  }

  .social { position: absolute; left: 47px; top: 360px; list-style: none; }
  .social__row { display: flex; align-items: center; height: 50px; margin-bottom: 14px; }
  .social__mark { width: 50px; height: 50px; border-radius: 8px; background: var(--bark); margin-right: 14px; flex: none; }
  .social__text { font-size: 33px; font-weight: 500; color: var(--bark); line-height: 1; padding-top: 6px; white-space: nowrap; }

  .badge-origin { position: absolute; left: 73px; top: 646px; width: 84px; height: 84px; border-radius: 50%; background: #2b2b2b; border: 4px solid #fff; }
  .badge-organic { position: absolute; left: 189px; top: 644px; width: 129px; height: 86px; background: var(--leaf); }

  .product-type {
    position: absolute; left: 370px; top: 532px; width: 464px; text-align: center;
    font-family: "Josefin Sans", sans-serif; font-weight: 600; font-size: 40px; line-height: 1;
    letter-spacing: 8px; white-space: nowrap; color: var(--bark);
  }
  .product-name {
    position: absolute; left: 380px; top: 598px; width: 440px; text-align: center; white-space: nowrap;
    font-family: "Lilita One", sans-serif; font-size: 74px; line-height: 1; color: var(--cocoa);
  }

  .ingredients {
    position: absolute; left: 850px; top: 302px; width: 305px; text-align: center;
    font-size: 38px; font-weight: 600; line-height: 41px; color: var(--bark);
  }

  .nutrition { position: absolute; left: 845px; top: 462px; width: 316px; }
  .nutrition__title { font-size: 33px; font-weight: 500; color: var(--cocoa); line-height: 38px; margin-left: 2px; white-space: nowrap; }
  .nutrition__table { width: 100%; border-collapse: collapse; table-layout: fixed; font-size: 18px; color: var(--bark); }
  .nutrition__table td { height: 24px; padding: 3px 0 0 3px; line-height: 1; white-space: nowrap; }
  .nutrition__table td.value { width: 134px; }
  .nutrition__table tr.is-band td { background: var(--band); color: #2a0e05; }
  .nutrition__table .indent-1 { padding-left: 12px; }
  .nutrition__table .indent-2 { padding-left: 17px; }

  .peanut-visual {
    position: absolute; left: 907px; top: 786px; width: 193px; height: 101px;
    border-radius: 50px; background: linear-gradient(160deg, var(--shell) 0%, #a47a48 55%, var(--kernel) 100%);
  }

  .allergy { position: absolute; left: 848px; top: 948px; width: 320px; color: var(--cocoa); }
  .allergy__title { font-size: 30px; font-weight: 500; line-height: 36px; }
  .allergy__text { font-size: 23px; font-weight: 500; line-height: 32px; white-space: nowrap; }

  .print-box {
    position: absolute; left: 48px; width: 296px; height: 146px; background: var(--paper);
    display: flex; align-items: center; justify-content: center;
    font-size: 31px; font-weight: 500; color: var(--bark);
  }
  .print-box--date { top: 828px; }
  .print-box--code { top: 995px; }

  .claims { position: absolute; left: 380px; top: 852px; list-style: none; }
  .claims li { display: flex; align-items: center; height: 37px; font-size: 33px; color: var(--bark); white-space: nowrap; }
  .claims svg { width: 22px; height: 26px; margin-right: 11px; flex: none; }

  .volume { position: absolute; left: 500px; top: 1100px; width: 200px; text-align: center; font-size: 38px; font-weight: 600; color: var(--cocoa); }
</style>
</head>
<body>
<main class="label">
  <div class="label__body"></div>
  <div class="label__arch"></div>
  <div class="brand-name">KirvaLume</div>
  <div class="mascot" role="img" aria-label="Illustrated mascot eating peanuts"></div>

  <ul class="social">
    <li class="social__row"><span class="social__mark"></span><span class="social__text">Kirvalume</span></li>
    <li class="social__row"><span class="social__mark"></span><span class="social__text">Kirvalume</span></li>
    <li class="social__row"><span class="social__mark"></span><span class="social__text">Kirvalume.co.uk</span></li>
  </ul>

  <div class="badge-origin" role="img" aria-label="Made in UK badge"></div>
  <div class="badge-organic" role="img" aria-label="Organic certification badge"></div>

  <div class="product-type">COLD PRESSED</div>
  <h1 class="product-name">Peanut Oil</h1>

  <p class="ingredients">Ingredients:<br>100% Organic<br>peanut oil</p>

  <section class="nutrition">
    <h2 class="nutrition__title">Nutrition Information</h2>
    <table class="nutrition__table">
      <tr class="is-band"><td>Typical values</td><td class="value">per 100g</td></tr>
      <tr><td>Energy</td><td class="value">kJ896/kCal3685</td></tr>
      <tr class="is-band"><td>Fat</td><td class="value">100g</td></tr>
      <tr><td class="indent-1">Of which Saturated</td><td class="value">19.7g</td></tr>
      <tr><td class="indent-2">Mono-unsaturated</td><td class="value">36.4g</td></tr>
      <tr><td class="indent-2">Poly-unsaturated</td><td class="value">43.4g</td></tr>
      <tr><td>Protein</td><td class="value">0.1g</td></tr>
      <tr class="is-band"><td>Carbohydrate</td><td class="value">&lt;0.5g</td></tr>
      <tr><td class="indent-1">Of which sugar</td><td class="value">&lt;0.1g</td></tr>
      <tr><td>Fibre</td><td class="value">&lt;0.5</td></tr>
    </table>
  </section>

  <div class="peanut-visual" role="img" aria-label="Photo of peanuts in shell with two kernels"></div>

  <section class="allergy">
    <h2 class="allergy__title">Allergy advice:</h2>
    <p class="allergy__text">Peanuts are packed on<br>premises that handles<br>cereals, nuts (including<br>peanuts), soya, sesame &amp;<br>products containing gluten.</p>
  </section>

  <div class="print-box print-box--date">best before date</div>
  <div class="print-box print-box--code">barcode</div>

  <ul class="claims">
    <li><svg viewBox="0 0 22 26"><path d="M2 14 L8 24 L20 2" fill="none" stroke="currentColor" stroke-width="2"/></svg>Organic</li>
    <li><svg viewBox="0 0 22 26"><path d="M2 14 L8 24 L20 2" fill="none" stroke="currentColor" stroke-width="2"/></svg>Vegan</li>
    <li><svg viewBox="0 0 22 26"><path d="M2 14 L8 24 L20 2" fill="none" stroke="currentColor" stroke-width="2"/></svg>High in Monounsaturated fat</li>
    <li><svg viewBox="0 0 22 26"><path d="M2 14 L8 24 L20 2" fill="none" stroke="currentColor" stroke-width="2"/></svg>High in Poly-unsaturated fat</li>
  </ul>

  <div class="volume">250ml</div>
</main>
</body>
</html>
```